Dietary supplement package design

We need a design for a range of dietary supplements mentioned below. The colors can be derived from the attached company logo and the package is a plastic bottle for medicines use (attached is a sample). All products will have the same package design and color with a permissible slight change to product name and associated picture/artwork (if any). Please avoid using pictures of humans or animals. We expect to see a label with three panels:
1. Left panel containing instructions, warnings and other information.
2. Front panel containing products name and its unique look
3. Right panel containing nutrient/ingredient information table and address.
The label will dual language (Arabic/English) and we have no issue to use special colors, i.e. UV, gold or silver.
Products names are:
1. Ginkgo biloba
2. Slimming formula
3. Fat Absorber
4. Glutathione
5. Royal Jelly
6. Vitamin D
Reason: Allow designers to provide more suggestions
Target Market(s)
Consumers and health care professionals
Industry/Entity Type
Healthcare
Look and feel

```html
<!DOCTYPE html>
<html lang="en">
<head>
<meta charset="utf-8">
<title>Apexa Supplement Labels</title>
<link rel="stylesheet" href="https://fonts.googleapis.com/css2?family=Saira+Condensed:wght@600;700&family=Roboto:wght@500;700&display=swap">
<style>
  :root {
    --page: #f6f6f6;
    --label-white: #ffffff;
    --silver: #b9bcc0;
    --silver-dark: #8e9297;
    --brand-blue: #1f5fb0;
    --brand-square: #1b3d7a;
    --tone-glutathione: #d61f26;
    --tone-royal-jelly: #5ea72c;
    --tone-ginkgo: #4a1f7e;
    --tone-vitamin-d: #f08c12;
    --tone-slimming: #1b3f9c;
    --tone-fat-absorber: #1f9a3b;
  }
  * { box-sizing: border-box; margin: 0; padding: 0; }
  html, body { width: 1200px; height: 900px; overflow: hidden; }
  body {
    background: var(--page);
    font-family: "Roboto", Arial, sans-serif;
    position: relative;
  }
  .label-range {
    position: absolute;
    left: 22px;
    top: 290px;
    display: flex;
    gap: 8px;
  }
  .label {
    position: relative;
    width: 186px;
    height: 320px;
    background: var(--label-white);
    box-shadow: 0 2px 10px rgba(0,0,0,0.10);
    overflow: hidden;
  }
  .label-rim {
    position: absolute;
    left: 0; right: 0; top: 12px;
    height: 6px;
    background: linear-gradient(180deg, var(--silver) 0%, #e6e7e9 50%, var(--silver-dark) 100%);
  }
  .brand {
    position: absolute;
    top: 36px; left: 0; right: 0;
    text-align: center;
    color: var(--brand-blue);
  }
  .brand-mark {
    display: block;
    width: 18px; height: 18px;
    margin: 0 auto 3px;
    background: var(--brand-square);
  }
  .brand-name {
    display: block;
    font-family: "Roboto", Arial, sans-serif;
    font-weight: 700;
    font-size: 17px;
    line-height: 1;
  }
  .brand-tagline {
    display: block;
    font-weight: 500;
    font-size: 6.5px;
    line-height: 1.4;
    margin-top: 1px;
  }
  .product-name {
    position: absolute;
    top: 100px; left: 0; right: 0;
    text-align: center;
    font-family: "Saira Condensed", "Arial Narrow", sans-serif;
    font-weight: 700;
    font-size: 30px;
    line-height: 1;
    white-space: nowrap;
    color: var(--tone);
  }
  .product-name.is-long { font-size: 25px; top: 103px; }
  .label-band {
    position: absolute;
    left: 0; bottom: 0;
    width: 186px; height: 180px;
    display: block;
  }
  .band-fill { fill: var(--tone); }
  .band-edge { fill: var(--silver); }
  .capsule-count {
    position: absolute;
    right: 6px; bottom: 48px;
    width: 30px;
    padding: 2px 0;
    border: 1px solid rgba(255,255,255,0.8);
    color: #fff;
    text-align: center;
    font-size: 5px;
    line-height: 1.2;
  }
  .capsule-count strong { display: block; font-size: 10px; }
  .label--glutathione { --tone: var(--tone-glutathione); }
  .label--royal-jelly { --tone: var(--tone-royal-jelly); }
  .label--ginkgo { --tone: var(--tone-ginkgo); }
  .label--vitamin-d { --tone: var(--tone-vitamin-d); }
  .label--slimming { --tone: var(--tone-slimming); }
  .label--fat-absorber { --tone: var(--tone-fat-absorber); }
</style>
</head>
<body>
<svg width="0" height="0" style="position:absolute">
  <defs>
    <radialGradient id="band-glow" cx="0.6" cy="0.65" r="0.6">
      <stop offset="0" stop-color="#ffffff" stop-opacity="0.45"/>
      <stop offset="1" stop-color="#ffffff" stop-opacity="0"/>
    </radialGradient>
    <symbol id="band-shape" viewBox="0 0 186 180">
      <path class="band-edge" d="M0 24 C70 40 130 30 186 6 L186 16 C130 40 70 50 0 34 Z"/>
      <path class="band-fill" d="M0 34 C70 50 130 40 186 16 L186 180 L0 180 Z"/>
      <path d="M0 34 C70 50 130 40 186 16 L186 180 L0 180 Z" fill="url(#band-glow)"/>
    </symbol>
  </defs>
</svg>

<main class="label-range">
  <article class="label label--glutathione">
    <div class="label-rim"></div>
    <div class="brand"><span class="brand-mark"></span><span class="brand-name">Apexa</span><span class="brand-tagline">NovaCare Health &amp; Supply</span></div>
    <h2 class="product-name">Glutathione</h2>
    <svg class="label-band" viewBox="0 0 186 180" role="img" aria-label="Red light-burst artwork band"><use href="#band-shape"/></svg>
    <div class="capsule-count"><strong>60</strong>Vegetarian Capsules</div>
  </article>

  <article class="label label--royal-jelly">
    <div class="label-rim"></div>
    <div class="brand"><span class="brand-mark"></span><span class="brand-name">Apexa</span><span class="brand-tagline">NovaCare Health &amp; Supply</span></div>
    <h2 class="product-name">Royal Jelly</h2>
    <svg class="label-band" viewBox="0 0 186 180" role="img" aria-label="Green light-burst artwork band"><use href="#band-shape"/></svg>
    <div class="capsule-count"><strong>60</strong>Vegetarian Capsules</div>
  </article>

  <article class="label label--ginkgo">
    <div class="label-rim"></div>
    <div class="brand"><span class="brand-mark"></span><span class="brand-name">Apexa</span><span class="brand-tagline">NovaCare Health &amp; Supply</span></div>
    <h2 class="product-name is-long">Ginkgo Biloba</h2>
    <svg class="label-band" viewBox="0 0 186 180" role="img" aria-label="Purple light-burst artwork band"><use href="#band-shape"/></svg>
    <div class="capsule-count"><strong>60</strong>Vegetarian Capsules</div>
  </article>

  <article class="label label--vitamin-d">
    <div class="label-rim"></div>
    <div class="brand"><span class="brand-mark"></span><span class="brand-name">Apexa</span><span class="brand-tagline">NovaCare Health &amp; Supply</span></div>
    <h2 class="product-name">Vitamin D</h2>
    <svg class="label-band" viewBox="0 0 186 180" role="img" aria-label="Orange light-burst artwork band"><use href="#band-shape"/></svg>
    <div class="capsule-count"><strong>60</strong>Vegetarian Capsules</div>
  </article>

  <article class="label label--slimming">
    <div class="label-rim"></div>
    <div class="brand"><span class="brand-mark"></span><span class="brand-name">Apexa</span><span class="brand-tagline">NovaCare Health &amp; Supply</span></div>
    <h2 class="product-name is-long">Slimming Formula</h2>
    <svg class="label-band" viewBox="0 0 186 180" role="img" aria-label="Blue light-burst artwork band"><use href="#band-shape"/></svg>
    <div class="capsule-count"><strong>60</strong>Vegetarian Capsules</div>
  </article>

  <article class="label label--fat-absorber">
    <div class="label-rim"></div>
    <div class="brand"><span class="brand-mark"></span><span class="brand-name">Apexa</span><span class="brand-tagline">NovaCare Health &amp; Supply</span></div>
    <h2 class="product-name is-long">Fat Absorber</h2>
    <svg class="label-band" viewBox="0 0 186 180" role="img" aria-label="Green light-burst artwork band"><use href="#band-shape"/></svg>
    <div class="capsule-count"><strong>60</strong>Vegetarian Capsules</div>
  </article>
</main>
</body>
</html>
```